Vantrell Law Letterhead

We need a new letterhead design for a Law Firm. The address for the law firm is 4817 Larkspur Boulevard, Suite 250, Houston, Texas 77342. Phone Number: 832-619-3057; Fax Number: 832-407-1694. The logo is uploaded to the project.

```html
<!DOCTYPE html>
<html lang="en">
<head>
<meta charset="utf-8">
<title>Vantrell Law Stationery</title>
<link href="https://fonts.googleapis.com/css2?family=Open+Sans:wght@400;600;700&display=swap" rel="stylesheet">
<style>
  :root {
    --backdrop: #e6e1e2;
    --paper: #f3f3f4;
    --navy: #2f416d;
    --red: #d0312d;
    --ink: #2b2b2f;
    --muted: #6a6a72;
    --rule: #c9c9ce;
  }
  * { box-sizing: border-box; margin: 0; padding: 0; }
  html, body { width: 1200px; height: 880px; overflow: hidden; }
  body {
    background: var(--backdrop);
    font-family: "Open Sans", Arial, sans-serif;
    color: var(--ink);
    position: relative;
  }
  .sheet { position: absolute; background: var(--paper); box-shadow: 0 8px 22px rgba(60,50,55,.18); }

  .brand { display: flex; align-items: center; gap: 8px; }
  .brand-dot { width: 14px; height: 14px; border-radius: 50%; background: var(--navy); flex: none; }
  .brand-name { font-weight: 600; color: var(--navy); letter-spacing: .06em; text-transform: uppercase; }
  .brand--light .brand-dot { background: #fff; }
  .brand--light .brand-name { color: #fff; }

  /* Envelope */
  .envelope { left: 40px; top: 130px; width: 270px; height: 560px; border-left: 6px solid var(--navy); }
  .envelope .brand { position: absolute; top: 28px; right: 22px; }
  .envelope .brand-name { font-size: 15px; }
  .envelope-address {
    position: absolute; left: 22px; bottom: 28px;
    font-size: 11px; line-height: 1.5; color: var(--muted);
    padding-left: 10px; border-left: 1px solid var(--rule);
  }

  /* Letterhead */
  .letterhead { left: 340px; top: 40px; width: 560px; height: 800px; border-bottom: 5px solid var(--navy); padding: 44px 52px; }
  .letterhead-header { display: flex; justify-content: space-between; align-items: flex-start; }
  .letterhead .brand-name { font-size: 19px; }
  .sender { font-size: 8.5px; line-height: 1.45; padding-left: 10px; border-left: 1px solid var(--rule); }
  .sender-name { font-weight: 700; text-transform: uppercase; letter-spacing: .03em; }
  .letter-body { margin-top: 56px; font-size: 9.5px; line-height: 1.6; color: #3b3b40; }
  .letter-body p { margin-bottom: 14px; }
  .closing { margin-top: 60px; font-size: 9.5px; }
  .signature { display: block; margin: 12px 0 6px; }
  .signer-title { font-size: 11px; }
  .letterhead-footer {
    position: absolute; left: 52px; right: 52px; bottom: 30px;
    display: flex; gap: 22px; font-size: 9px; line-height: 1.5; color: var(--muted);
  }
  .footer-block { padding-left: 10px; border-left: 1px solid var(--rule); }
  .label { color: var(--red); font-weight: 600; }

  /* Business cards */
  .card { width: 260px; height: 150px; }
  .card--front { left: 920px; top: 150px; background: var(--navy); display: flex; align-items: center; justify-content: center; }
  .card--front .brand-name { font-size: 17px; }
  .card--back { left: 920px; top: 340px; padding: 20px; display: flex; justify-content: space-between; }
  .card--back .brand { align-self: flex-end; }
  .card--back .brand-name { font-size: 11px; }
  .card-details { font-size: 8px; line-height: 1.5; color: var(--muted); text-align: left; }
  .card-name { font-size: 13px; font-weight: 600; color: var(--ink); }
  .card-role { margin-bottom: 8px; }
  .card-gap { margin-top: 6px; }
</style>
</head>
<body>

<section class="sheet envelope">
  <div class="brand"><span class="brand-dot"></span><span class="brand-name">Vantrell Law</span></div>
  <address class="envelope-address">
    4817 Larkspur Boulevard,<br>Suite 250, Houston,<br>Texas 77342
  </address>
</section>

<section class="sheet letterhead">
  <header class="letterhead-header">
    <div class="brand"><span class="brand-dot"></span><span class="brand-name">Vantrell Law</span></div>
    <div class="sender">
      <div class="sender-name">Daniel R. Ashford</div>
      <div class="sender-name">Attorney</div>
      <div>832-619-3057</div>
      <div>contact@vantrellinjury.com</div>
    </div>
  </header>

  <div class="letter-body">
    <p>Lorem Ipsum,</p>
    <p>Lorem ipsum dolor sit amet, consectetur adipiscing elit. Donec orci purus, luctus vitae dignissim a, iaculis in nisi. Vivamus faucibus, ipsum nec aliquet viverra, leo mauris condimentum ligula, sit amet sagittis leo lectus at nunc. Praesent egestas tortor id nisi porttitor mattis. In tortor ante, ultricies in suscipit a, tempus non massa. Vivamus et auctor mi. Fusce vel massa nulla. Phasellus nec eros mauris, et scelerisque orci.</p>
    <p>Donec malesuada orci vitae nulla accumsan porta a id massa. Quisque accumsan iaculis magna, eget tincidunt semper, odio nibh rutrum mi, id feugiat ante nisi eu risus. Vestibulum nunc orci, rhoncus a placerat in, ultricies in mi. Quisque scelerisque sagittis nulla at porttitor. Maecenas consequat, magna eget tincidunt semper, odio eros, vel fringilla nisi suscipit eget. Cras mattis varius nibh rutrum mi, id feugiat ante nisi eu risus.</p>
    <p>Sed id augue vitae urna euismod commodo aliquet a quam. Pellentesque arcu velit, cursus et malesuada ut, consequat et diam. Nullam erat sem, rhoncus id ullamcorper vitae, rhoncus et arcu. In ultricies ultricies nulla, ut rutrum nisi iaculis at. Donec eu magna a metus ornare faucibus. Fusce aliquet faucibus ultricies. Morbi semper sem arcu adipiscing lacus, ac bibendum nulla leo eu purus. Quisque nec diam sed risus commodo nibh. Vestibulum id purus lorem.</p>
  </div>

  <div class="closing">
    <div>Sincerely,</div>
    <svg class="signature" width="130" height="34" role="img" aria-label="Handwritten signature of Jordan Mills">
      <rect width="130" height="34" rx="4" fill="#e4e4e7"/>
    </svg>
    <div class="signer-title">Company Director</div>
  </div>

  <footer class="letterhead-footer">
    <div class="footer-block">4817 Larkspur Boulevard,<br>Suite 250, Houston,<br>Texas 77342</div>
    <div class="footer-block">
      <span class="label">T:</span> 832-619-3057<br>
      <span class="label">F:</span> 832-407-1694<br>
      www.vantrellinjury.com
    </div>
  </footer>
</section>

<section class="sheet card card--front">
  <div class="brand brand--light"><span class="brand-dot"></span><span class="brand-name">Vantrell Law</span></div>
</section>

<section class="sheet card card--back">
  <div class="brand"><span class="brand-dot"></span><span class="brand-name">Vantrell Law</span></div>
  <div class="card-details">
    <div class="card-name">Daniel R. Ashford</div>
    <div class="card-role">Attorney</div>
    <div>832-619-3057</div>
    <div>contact@vantrellinjury.com</div>
    <div class="card-gap">2215 W Fairmont St.</div>
    <div>Houston, Texas 77019</div>
  </div>
</section>

</body>
</html>
```